Brightwave Learners Agency business cards

Australian company about to start offering its services. We recruit international students to come to study English, vocational education and postgraduate courses in Australia. We help them find the institution and select the right city they want to come to Australia. We are a young, online oriented and supportive agency. Our clients are between 18 and 35 years old, mainly University students, young professionals or people with work experience. We provide much more information that any other agency offer. We administrate a Facebook group with more than 11.000 members that daily ask questions about general information when coming to Australia, while they are here and even after they leave the country

Target Market(s)

International students from South America, Central America and Europe

Industry/Entity Type

Student

Contact Information for Business Card

Tomas Velorin
Managing Director
tomas@kelvona.com.au
www.kelvrona.com.au
+61 497285064
Melbourne, Australia

Font styles to use
Serif
Sans Serif

Colors

Designer to choose colors to be used in the design.

Requirements
Must have
• Horizontal design
• Standard business card size and shape. If font uses green or yellow colours, they will have to match the ones from the logo
Nice to have
• UPDATE: Use the contents of the green image to design one of the card sides. Use our logo in the background of that side as watermark.
• Passport image, or immigration stamps. A picture of the Yarra River (from Melbourne) would be cool as well.
Should not have
• Non-standard business card size and shape
• Not black as the background colour of any sides as we are not a VIP agency or a hight class service. We are orientes to young people and they like colours, pictures, something attractive.
• Vertical design
• NO YELLOW or BLACK AS THE BACKGROUND COLOUR OF ANY SIDE OF THE BIZ CARD

```html
<!DOCTYPE html>
<html lang="en">
<head>
<meta charset="utf-8">
<title>Brightwave Learners Agency – Business Cards</title>
<link rel="stylesheet" href="https://fonts.googleapis.com/css2?family=Poppins:wght@400;500;600&display=swap">
<style>
  :root {
    --paper: #ecebe6;
    --card-white: #ffffff;
    --brand-green: #0f6a43;
    --brand-yellow: #e8bd22;
    --ink: #3a3a3a;
    --night-top: #2a3548;
    --night-mid: #3c4a5c;
    --river: #4f5e6c;
    --white: #ffffff;
  }
  * { box-sizing: border-box; margin: 0; padding: 0; }
  html, body {
    width: 1200px; height: 929px; overflow: hidden;
    background: var(--paper);
    font-family: "Poppins", sans-serif;
  }
  .stage { position: relative; width: 1200px; height: 929px; }

  .card {
    position: absolute;
    width: 520px; height: 300px;
    overflow: hidden;
    box-shadow: 0 6px 18px rgba(0,0,0,0.18);
  }

  /* Front side */
  .card-front { left: 110px; top: 110px; }
  .front-photo {
    position: absolute; inset: 0;
    background: linear-gradient(160deg, var(--night-top) 0%, var(--night-mid) 45%, var(--river) 100%);
  }
  .front-content {
    position: absolute; inset: 0;
    display: flex; flex-direction: column; align-items: center; justify-content: center;
    color: var(--white);
  }
  .front-brand { font-size: 50px; font-weight: 600; letter-spacing: 0.5px; line-height: 1; }
  .front-tagline { margin-top: 44px; font-size: 13px; font-weight: 400; }

  /* Back side */
  .card-back { left: 570px; top: 510px; background: var(--card-white); }
  .back-swoosh { position: absolute; inset: 0; }
  .holder {
    position: absolute; left: 22px; top: 34px;
    color: var(--white); white-space: nowrap;
  }
  .holder-name { font-size: 18px; font-weight: 500; letter-spacing: 0.6px; }
  .holder-role { font-size: 12px; font-weight: 400; margin-left: 4px; }

  .back-brand {
    position: absolute; left: 120px; top: 196px;
    display: flex; align-items: center; gap: 10px;
  }
  .back-brand-dot { width: 14px; height: 14px; border-radius: 50%; background: var(--brand-yellow); }
  .back-brand-name { font-size: 36px; font-weight: 600; color: var(--brand-green); line-height: 1; }

  .contact {
    position: absolute; right: 26px; top: 122px;
    list-style: none; text-align: right;
    font-size: 12px; color: var(--ink); line-height: 1.75;
  }
  .contact li { display: flex; justify-content: flex-end; align-items: center; gap: 8px; }
  .contact .web-domain { color: var(--brand-green); }
  .contact svg { width: 11px; height: 11px; flex: none; }
</style>
</head>
<body>
<main class="stage">

  <section class="card card-front">
    <div class="front-photo" role="img" aria-label="Evening photograph of the Yarra River running through Melbourne's city skyline"></div>
    <div class="front-content">
      <div class="front-brand">Kelvrona</div>
      <p class="front-tagline">Hacemos más por ti!</p>
    </div>
  </section>

  <section class="card card-back">
    <svg class="back-swoosh" viewBox="0 0 520 300" width="520" height="300" aria-hidden="true">
      <path d="M0 0 H340 C332 70 270 95 190 125 C120 150 84 205 76 300 H0 Z" fill="var(--brand-yellow)"/>
      <path d="M0 0 H326 C318 62 258 86 180 116 C110 142 72 200 64 300 H0 Z" fill="var(--brand-green)"/>
    </svg>

    <div class="holder">
      <span class="holder-name">TOMAS VELORIN –</span><span class="holder-role">Managing Director</span>
    </div>

    <div class="back-brand">
      <span class="back-brand-name">Kelvrona</span>
      <span class="back-brand-dot"></span>
    </div>

    <ul class="contact">
      <li>Melbourne, Australia</li>
      <li>+61 497285064
        <svg viewBox="0 0 12 12"><rect x="3" y="0.8" width="6" height="10.4" rx="1.2" fill="none" stroke="var(--brand-green)" stroke-width="1.3"/></svg>
      </li>
      <li>tomas@kelvona.com.au
        <svg viewBox="0 0 12 12"><rect x="0.5" y="2.5" width="11" height="7" fill="var(--brand-green)"/><path d="M0.5 2.5 L6 6.5 L11.5 2.5" fill="none" stroke="#fff" stroke-width="1"/></svg>
      </li>
      <li><span>www.<span class="web-domain">kelvrona.com.au</span></span>
        <svg viewBox="0 0 12 12"><circle cx="5" cy="5" r="3.4" fill="none" stroke="var(--brand-green)" stroke-width="1.6"/><path d="M7.5 7.5 L11 11" stroke="var(--brand-green)" stroke-width="1.8"/></svg>
      </li>
    </ul>
  </section>

</main>
</body>
</html>
```